Harborline Kidney Services Brochure - Marketing brochure for a dialysis company in the USA

I want a brochure to be created for my business. I have a brochure that can be used as a comparison. My old Company name is Bluewater Renal Infusion Partners. The new Company Name is Harborline Kidney Services. I have a sample of the Old Brochure. and I uploaded the Logo of HKS. It will be used by my sales agents to introduce my company to potential client hospitals.

Target Market(s)

CEOs of Acute Hospitals and Medical Centers

Industry/Entity Type

Health Care

Requirements
Must have
• Use the sample as a guide. This project is for a 4 page brochure. (2 letter size pages folded in half crosswise) Use the text from the old brochure to the new brochure, replacing the old info with the new company info as needed.
Nice to have
• Here is my company info:
• Harborline Kidney Services
• 4180 W 61st Ave
• Suite D
• It will be nice if the designer can give me the project files that would allow me to edit the text of the brochure.
• McAllen, TX 78392
• (956) 417-2863
• admin@HarborlineKidneyLLC.example
• www.harborlinekidney.example

```html
<!DOCTYPE html>
<html lang="en">
<head>
<meta charset="utf-8">
<title>Harborline Kidney Services – Brochure Spreads</title>
<link href="https://fonts.googleapis.com/css2?family=Oswald:wght@400;500&family=Open+Sans:wght@400;600;700&family=Montserrat:wght@600;700&display=swap" rel="stylesheet">
<style>
:root{
  --blue:#1a9be6;
  --blue-deep:#0d79c8;
  --red:#e21b23;
  --ink:#333;
  --white:#fff;
}
*{box-sizing:border-box;margin:0;padding:0}
html,body{width:1200px;height:1200px;overflow:hidden}
body{background:radial-gradient(ellipse at 50% 45%,#f2f2f2 0%,#dcdcdc 70%,#cfcfcf 100%);font-family:'Open Sans',sans-serif;color:var(--ink);position:relative}
.board-label{position:absolute;font-family:'Open Sans',sans-serif;font-size:27px;color:#111;font-weight:400}
.spread{position:absolute;width:501px;height:354px;display:flex;box-shadow:0 2px 6px rgba(0,0,0,.25);background:var(--white)}
.page{position:relative;width:50%;height:100%;overflow:hidden;background:linear-gradient(180deg,#fff 0%,#f3f3f3 100%)}
.page svg.deco{position:absolute;left:0;top:0;width:100%;height:100%}
.content{position:absolute;inset:0}
.block{position:absolute}
.wordmark{position:absolute;text-align:center;line-height:1;white-space:nowrap}
.wordmark .mark{font-family:'Oswald',sans-serif;font-weight:500;font-size:30px;color:var(--blue-deep);letter-spacing:1px}
.wordmark .sub{font-family:'Oswald',sans-serif;font-size:5.5px;color:#222;letter-spacing:.2px;margin-top:1px}
.q{font-family:'Oswald',sans-serif;color:var(--red);font-size:5.6px;text-transform:uppercase;line-height:1.25;margin-bottom:4px}
.body{font-size:4.3px;line-height:1.35;color:#444;text-align:justify;margin-bottom:6px}
.call{font-family:'Montserrat',sans-serif;color:var(--red);font-weight:600;font-size:11px;text-align:center;line-height:1.2}
.web{font-family:'Montserrat',sans-serif;font-weight:700;font-size:7px;color:#222;text-align:center;line-height:1.2}
.photo{position:absolute;border-radius:2px}
.boxed{position:absolute;border:1.2px solid var(--red);border-radius:8px;padding:6px}
.list{list-style:none}
.list li{position:relative;padding-left:13px;font-size:4.2px;line-height:1.35;color:#444;text-align:justify;margin-bottom:6px}
.list li::before{content:"";position:absolute;left:0;top:1px;width:7px;height:7px;background:var(--red)}
.list li span{position:absolute;left:2.2px;top:1px;color:#fff;font-size:5px;font-weight:700}
/* back cover */
.back{background:linear-gradient(160deg,#2aa6ef 0%,var(--blue-deep) 100%)}
.back h3{position:absolute;top:24px;width:100%;text-align:center;font-family:'Montserrat',sans-serif;font-size:8px;color:#fff}
.back .intro{position:absolute;top:38px;left:28px;right:28px;text-align:center;color:#fff;font-size:6px;line-height:1.3;font-weight:600}
.circle-photo{position:absolute;border-radius:50%;border:3px solid var(--red);box-shadow:0 0 0 2px #fff}
.contact{position:absolute;top:176px;width:100%;text-align:center}
.contact h2{font-family:'Montserrat',sans-serif;font-weight:700;font-size:17px;color:#333;margin-bottom:4px}
.contact p{font-size:7.4px;line-height:1.3;color:#333}
.contact b{color:var(--red)}
.socials{display:flex;justify-content:center;gap:7px;margin-top:7px}
.socials i{display:block;width:15px;height:15px;border-radius:50%;background:var(--red)}
.mission{position:absolute;top:292px;width:100%;text-align:center;color:#fff}
.mission h4{font-family:'Montserrat',sans-serif;font-size:8px;color:#222;margin-bottom:3px;line-height:1.1}
.mission p{font-size:5.2px;line-height:1.35;padding:0 20px}
.mission .web{color:#222;margin-top:8px;font-size:6.5px}
/* front */
.front .headline{position:absolute;top:282px;width:100%;text-align:center;font-family:'Oswald',sans-serif;line-height:1.1}
.front .headline .l1{font-size:16px;color:#222}
.front .headline .l2{font-size:16px;color:var(--blue-deep)}
.front .headline .l3{font-family:'Montserrat',sans-serif;font-weight:600;font-size:9px;color:#222;margin-top:3px}
</style>
</head>
<body>

<div class="board-label" style="left:175px;top:165px">Back</div>
<div class="board-label" style="left:407px;top:165px">Front</div>
<div class="board-label" style="left:710px;top:176px">Page 1</div>
<div class="board-label" style="left:915px;top:176px">Page 2</div>
<div class="board-label" style="left:175px;top:635px">Page 3</div>
<div class="board-label" style="left:398px;top:635px">Page 4</div>
<div class="board-label" style="left:715px;top:635px">Page 5</div>
<div class="board-label" style="left:918px;top:635px">Page 6</div>

<!-- SPREAD: back + front -->
<div class="spread" style="left:72px;top:237px">
  <section class="page back">
    <svg class="deco" viewBox="0 0 250 354" preserveAspectRatio="none">
      <path d="M0 118 C70 90 170 120 250 100 V280 C170 265 80 310 0 280Z" fill="#fff"/>
      <path d="M0 280 C80 310 170 265 250 280" stroke="var(--red)" stroke-width="5" fill="none"/>
      <path d="M0 118 C70 90 170 120 250 100" stroke="var(--red)" stroke-width="3" fill="none"/>
    </svg>
    <h3>HARBORLINE KIDNEY SERVICES</h3>
    <p class="intro">We provide hemodialysis services to Acute Hospitals, LTACHs, and Acute Rehabilitation Hospitals. We offer flat rate pricing per case.</p>
    <div class="circle-photo" role="img" aria-label="Photo of a nurse attending a patient in bed" style="left:16px;top:84px;width:62px;height:62px;background:radial-gradient(circle,#d8e6f0,#8fb6cf)"></div>
    <div class="circle-photo" role="img" aria-label="Photo of clinical staff in a hospital room" style="left:116px;top:84px;width:56px;height:56px;background:radial-gradient(circle,#e6dcd0,#a9b8c4)"></div>
    <div class="circle-photo" role="img" aria-label="Photo of a patient receiving treatment" style="left:194px;top:122px;width:46px;height:46px;background:radial-gradient(circle,#e2d8cc,#9db3c3)"></div>
    <div class="contact">
      <h2>CONTACT US</h2>
      <p><b>Phone:</b> (956) 417-2863</p>
      <p><b>Fax:</b> (956) 402-5518</p>
      <p><b>Mail:</b> admin@HarborlineKidneyLLC.example</p>
      <div class="socials"><i></i><i></i><i></i></div>
    </div>
    <div class="mission">
      <h4>Mission statement</h4>
      <p>To provide innovative, cutting-edge healthcare service to our clients while adhering to the timeless teachings of our founding faith.</p>
      <div class="web">www.harborlinekidney.example</div>
    </div>
  </section>
  <section class="page front">
    <svg class="deco" viewBox="0 0 250 354" preserveAspectRatio="none">
      <path d="M150 0 H250 V90 C230 40 200 15 150 0Z" fill="var(--red)"/>
      <path d="M250 170 C240 250 180 272 110 280 C170 282 225 275 250 262Z" fill="var(--red)"/>
      <path d="M28 110 C28 72 70 58 110 58 H200 C225 58 232 75 232 100 V240 C232 266 210 274 180 274 H60 C35 274 28 262 28 240Z" fill="var(--blue)"/>
      <rect x="0" y="342" width="250" height="12" fill="var(--red)"/>
      <rect x="0" y="338" width="250" height="4" fill="var(--blue)"/>
    </svg>
    <div class="wordmark" style="left:14px;top:12px;width:96px">
      <div class="mark">HKS</div>
      <div class="sub">HARBORLINE KIDNEY SERVICES</div>
    </div>
    <div class="photo" role="img" aria-label="Photo of a nurse preparing a seated patient for dialysis" style="left:34px;top:64px;width:192px;height:204px;border-radius:40px 10px 30px 10px;background:linear-gradient(135deg,#eef3f6 0%,#bcd3e0 45%,#7fa8c2 100%)"></div>
    <div class="headline">
      <div class="l1">Tired of paying outrageous</div>
      <div class="l2">prices for inpatient dialysis?</div>
      <div class="l3">CALL US NOW (956) 417-2863</div>
    </div>
  </section>
</div>

<!-- SPREAD: page 1 + page 2 -->
<div class="spread" style="left:617px;top:233px">
  <section class="page">
    <svg class="deco" viewBox="0 0 250 354" preserveAspectRatio="none">
      <path d="M0 0 H250 V6 C180 4 110 0 40 30 C25 37 10 45 0 50Z" fill="var(--blue)"/>
      <path d="M0 50 C40 20 120 0 250 6" stroke="var(--red)" stroke-width="4" fill="none"/>
      <rect x="0" y="343" width="250" height="11" fill="var(--blue)"/>
    </svg>
    <div class="wordmark" style="left:160px;top:26px;width:80px"><div class="mark">HKS</div><div class="sub">HARBORLINE KIDNEY SERVICES</div></div>
    <div class="content" style="padding:68px 16px 0 18px">
      <div class="q">Who is HKS and what services does it provide?</div>
      <p class="body">Harborline is the lowest cost, highest quality inpatient dialysis and related services provider in South Texas. HKS has achieved its excellent reputation by offering performance instead of promises.</p>
      <p class="body">Any company can tell you that they provide excellent service. Let us show you truly excellent service instead!</p>
    </div>
    <div class="boxed" style="left:12px;top:132px;width:228px;height:140px">
      <div class="q">Our facility currently contracts with another dialysis services provider.<br>Why should we switch to HKS?</div>
      <div class="photo" role="img" aria-label="Photo of a dialysis machine" style="left:6px;top:30px;width:34px;height:80px;background:linear-gradient(180deg,#e9eef2,#b9c6d0)"></div>
      <div style="margin-left:42px">
        <p class="body">HKS specializes in inpatient dialysis only. Your current provider specializes in outpatient, clinic based dialysis, and sends poorly qualified staff from their clinic to your facility to dialyze your often medically complex and hemodynamically unstable hospitalized patients. Contracting with a company that specializes in outpatient dialysis is similar to hiring a general practitioner to do neurosurgery.</p>
        <p class="body">Inpatient acute dialysis is a specialty, with much sicker and medically unstable clients than an outpatient dialysis clinic, and is best handled by a company that specializes ONLY in inpatient acute dialysis and related inpatient services.</p>
      </div>
    </div>
    <div class="block" style="left:18px;top:283px;width:216px">
      <div class="q" style="text-align:center">What types of facilities typically contract with HKS?</div>
      <p class="body">All types of inpatient facilities can contract with HKS, including large university medical centers, small community hospitals, long term acute care hospitals, and rehabilitation hospitals.</p>
    </div>
    <div class="web" style="position:absolute;top:324px;width:100%">www.harborlinekidney.example</div>
  </section>
  <section class="page">
    <svg class="deco" viewBox="0 0 250 354" preserveAspectRatio="none">
      <path d="M60 0 H250 V20 C200 30 130 10 60 0Z" fill="var(--blue)"/>
      <path d="M50 0 C120 12 190 30 250 22" stroke="var(--red)" stroke-width="4" fill="none"/>
      <rect x="0" y="343" width="250" height="11" fill="var(--red)"/>
    </svg>
    <div class="wordmark" style="left:12px;top:26px;width:80px"><div class="mark">HKS</div><div class="sub">HARBORLINE KIDNEY SERVICES</div></div>
    <ul class="list" style="position:absolute;left:16px;top:72px;width:222px">
      <li><span>1</span>Our contracts are very flexible, so you have the ability to contract for only those services that your facility needs. If you have a need for hemodialysis only, we will tailor your contract to suit your needs. If, in the future, you wish to add other services, a contract addendum can be completed quickly.</li>
      <li><span>2</span>Patient satisfaction is our top priority. If a patient is happy with our inpatient dialysis services, that patient will probably return to your facility when future medical services are needed. Thus, both of us will benefit from future revenue generated by that patient's return to your hospital. We actually do patient satisfaction surveys, and act upon the results. Our competition does not do this.</li>
      <li><span>3</span>We strive to cater to the needs of the nephrologist. We realize that nephrologists are a key driver of hospital inpatient dialysis volume. As such, we seek to cater to their needs.</li>
      <li><span>4</span>Any dialysis company can pass an inspection when they know a week or two in advance that the surveyors are coming. In this era of drop-in inspections, you need an inpatient dialysis provider that is always ready for inspection without advance notice. We stand ready for survey 365 days per year.</li>
      <li><span>5</span>The HKS education department is very familiar with the accreditation requirements for staff credentialing and competencies, and strives to ensure that each of our staff members is compliant at all times. In addition, HKS staff receives annual retraining in such areas as life safety, infection control, and privacy compliance.</li>
    </ul>
    <div class="q" style="position:absolute;top:244px;width:100%;text-align:center;font-size:8px;text-transform:none">How can I find out more about HKS and its services?</div>
    <p class="body" style="position:absolute;left:18px;top:262px;width:154px">The HKS education department is very familiar with the accreditation requirements for staff credentialing and competencies, and strives to ensure that each of our staff members is compliant at all times. In addition, staff receives annual retraining in life safety, infection control and privacy compliance.</p>
    <div class="photo" role="img" aria-label="Photo of clinicians in a laboratory" style="left:182px;top:262px;width:56px;height:36px;background:linear-gradient(135deg,#b8c9da,#6c8fb3)"></div>
    <div class="call" style="position:absolute;top:312px;width:100%">CALL US NOW (956) 417-2863</div>
  </section>
</div>

<!-- SPREAD: page 3 + page 4 -->
<div class="spread" style="left:72px;top:690px">
  <section class="page">
    <svg class="deco" viewBox="0 0 250 354" preserveAspectRatio="none">
      <path d="M0 0 H250 V18 C170 0 90 10 0 32Z" fill="var(--blue)"/>
      <path d="M0 34 C90 12 170 2 250 20" stroke="var(--red)" stroke-width="4" fill="none"/>
      <rect x="0" y="343" width="250" height="11" fill="var(--blue)"/>
    </svg>
    <div class="wordmark" style="left:168px;top:42px;width:72px"><div class="mark">HKS</div><div class="sub">HARBORLINE KIDNEY SERVICES</div></div>
    <div class="q" style="position:absolute;left:16px;top:58px;font-size:7px">How is HKS different from<br>its competitors?</div>
    <ul class="list" style="position:absolute;left:16px;top:92px;width:222px">
      <li><span>1</span>We are based in South Texas. Our two main competitors are based in other states. When you have a question or concern, you can contact the president and founder of Harborline by mobile phone, 24 hours a day, 7 days a week. You cannot do this with any of our competitors.</li>
      <li><span>2</span>Acute inpatient dialysis and related services is our ONLY business. We perform these treatments using cutting edge dialysis equipment. 95% of the business of our competitors comes from their outpatient hemodialysis clinics. Our competitors view their inpatient dialysis programs as "cash cows" that supplement the meager earnings of their outpatient clinics. They use their newest dialysis machines in their outpatient clinics, and send their outdated, discontinued equipment to their inpatient dialysis programs. Quite simply, inpatient dialysis is not their priority.</li>
      <li><span>3</span>We strive to seamlessly integrate with your patient care staff. One of our competitors requires a hospital ICU nurse to stand at the bedside with the dialysis staff member during the entire bedside dialysis treatment in the ICU. Such a practice is not only ridiculous, it is an added expense for your facility. Such a practice would never occur with HKS.</li>
      <li><span>4</span>We are committed to being an ethical partner. We realize that finding nurses for hire is sometimes challenging. Therefore, we make it a point not to hire away nurses from the facilities with which we contract.</li>
      <li><span>5</span>We place tremendous power in the hands of our frontline managers. Unlike our competitors, when equipment and other resources are needed, our frontline managers don't have to go through fifteen layers of middle management to get what they need. They simply call our president or vice president, and a decision is made quickly and locally.</li>
      <li><span>6</span>We offer more inpatient services more cost effectively than any of our competitors. Our inpatient services include hemodialysis, peritoneal dialysis, continuous venovenous hemodialysis, therapeutic apheresis, PICC line insertion and hemoperfusion.</li>
    </ul>
    <div class="call" style="position:absolute;top:309px;width:100%">CALL US NOW (956) 417-2863</div>
    <div class="web" style="position:absolute;top:325px;width:100%">www.harborlinekidney.example</div>
  </section>
  <section class="page">
    <svg class="deco" viewBox="0 0 250 354" preserveAspectRatio="none">
      <path d="M70 0 H250 V60 C220 20 150 5 70 0Z" fill="var(--blue)"/>
      <path d="M60 0 C150 8 210 20 250 60" stroke="var(--red)" stroke-width="4" fill="none"/>
      <rect x="0" y="343" width="250" height="11" fill="var(--red)"/>
    </svg>
    <div class="photo" role="img" aria-label="Illustration of an IV catheter" style="left:18px;top:8px;width:50px;height:28px;background:linear-gradient(135deg,#dfeaf2,#8fb9d8)"></div>
    <div class="block" style="left:14px;top:58px;width:222px">
      <div class="q">How does an HKS inpatient dialysis contract work?</div>
      <p class="body">If you decide to contract with us, we provide all the dialysis staff, dialysis specific machines, dialysis water treatment system, dialysis specific supplies, dialysis specific biomedical services, dialysis specific paperwork, dialysis specific policies and procedures, and accreditation required competencies and credentialing for our staff all for <b>one flat fee per treatment.</b></p>
      <p class="body">When the nephrologist writes a treatment order, Harborline staff perform that treatment according to the nephrologist's exact specifications. Dialysis treatments can be performed either at the bedside or in a separate dialysis room.</p>
    </div>
    <div class="boxed" style="left:14px;top:156px;width:226px;height:176px">
      <div class="photo" role="img" aria-label="Photo of a patient with a clinician" style="left:8px;top:10px;width:50px;height:38px;background:linear-gradient(135deg,#d9e3ea,#9fb7c9)"></div>
      <div style="margin-left:58px">
        <div class="q">Does HKS have satisfied customers<br>who can provide references?</div>
        <p class="body">We will be more than happy to provide you with a list of satisfied customers and nephrologists.</p>
      </div>
      <div class="photo" role="img" aria-label="Photo of a dialysis machine" style="left:6px;top:64px;width:40px;height:104px;background:linear-gradient(180deg,#eef2f5,#b5c4cf)"></div>
      <div style="margin-left:44px;margin-top:14px">
        <div class="q">Who are Harborline's competitors?</div>
        <p class="body">Two large dialysis companies, based in other states and other regions, provide most of the chronic outpatient and acute inpatient dialysis in the United States. In many locations, one of these two companies is the only dialysis provider in town, and can charge their hospital clients outrageous prices for acute inpatient dialysis services. Their business focus is chronic outpatient dialysis, so their focus is DEFINITELY NOT inpatient dialysis services. Since reimbursement is very meager for chronic outpatient dialysis services, the profitability of a typical dialysis clinic is only about 5% at best. By adding inpatient dialysis to its menu of services, a dialysis outpatient clinic can boost its profitability by several percentage points at your expense.</p>
      </div>
    </div>
  </section>
</div>

<!-- SPREAD: page 5 + page 6 -->
<div class="spread" style="left:617px;top:690px">
  <section class="page">
    <svg class="deco" viewBox="0 0 250 354" preserveAspectRatio="none">
      <path d="M0 0 H250 V4 C170 0 80 10 0 30Z" fill="var(--blue)"/>
      <path d="M0 32 C80 10 170 2 250 6" stroke="var(--red)" stroke-width="4" fill="none"/>
      <rect x="0" y="343" width="250" height="11" fill="var(--blue)"/>
    </svg>
    <div class="wordmark" style="left:168px;top:30px;width:72px"><div class="mark">HKS</div><div class="sub">HARBORLINE KIDNEY SERVICES</div></div>
    <div class="block" style="left:18px;top:56px;width:218px">
      <div class="q">Why are HKS prices so low in comparison<br>to the competition?</div>
      <p class="body">We do a huge volume of inpatient dialysis treatments, which allows us to purchase large quantities of supplies at lower prices. Unlike our competition, we don't have fifteen layers of management and millions of shareholders to support. In addition, our innovative staff compensation programs, and low turnover help keep our costs low.</p>
      <div class="q">Does HKS charge "add-on" fees for after-hours,<br>weekend, callback, or holiday treatments?</div>
      <p class="body">No. We charge one flat fee per inpatient dialysis treatment, regardless of when it is performed.</p>
      <div style="width:150px">
        <div class="q">What are the qualifications of the HKS staff?</div>
        <p class="body">Our staff is experienced in inpatient dialysis and related services. HKS staff are BCLS certified, and can be ACLS certified by our education department on request. All HKS staff receive comprehensive pre-hire drug testing and background checks.</p>
        <div class="q">Is HKS staff available for stat, on-call,<br>and after-hours treatments?</div>
        <p class="body">Yes. Part of our commitment to your facility involves being on-call to perform inpatient dialysis treatments 24 hours a day, 7 days a week.</p>
      </div>
      <div class="q">Does HKS employ a biomedical staff to maintain its equipment?</div>
      <p class="body">Yes. We have a full time, fully trained and credentialed biomedical staff. Copies of our machine maintenance and repair records are kept on site at your facility for compliance purposes. Like our dialysis staff, our biomedical staff is available 24 hours a day, 7 days a week.</p>
    </div>
    <div class="photo" role="img" aria-label="Photo of a gloved hand holding a blood sample tube" style="left:178px;top:152px;width:56px;height:74px;background:linear-gradient(135deg,#f1f1f1,#c7d2da)"></div>
    <div class="call" style="position:absolute;top:309px;width:100%">CALL US NOW (956) 417-2863</div>
    <div class="web" style="position:absolute;top:325px;width:100%">www.harborlinekidney.example</div>
  </section>
  <section class="page">
    <svg class="deco" viewBox="0 0 250 354" preserveAspectRatio="none">
      <path d="M80 0 H250 V40 C210 15 150 4 80 0Z" fill="var(--blue)"/>
      <path d="M70 0 C150 6 210 18 250 42" stroke="var(--red)" stroke-width="4" fill="none"/>
      <rect x="0" y="343" width="250" height="11" fill="var(--red)"/>
    </svg>
    <div class="block" style="left:14px;top:50px;width:222px">
      <div class="q">Is HKS insured?</div>
      <p class="body">Yes. Harborline maintains comprehensive malpractice, workers' compensation, and employee health insurance coverage.</p>
    </div>
    <div class="block" style="left:14px;top:96px;width:222px">
      <div class="q">What CQI/QA support does HKS provide?</div>
      <p class="body">We provide monthly inpatient dialysis specific CQI/QA in full collaboration with your infection control department and other departments/committees. We also provide monthly water culture and LAL testing of our equipment, and yearly water testing of our equipment.</p>
    </div>
    <div class="q" style="position:absolute;left:14px;top:148px">Does Harborline offer therapeutic apheresis?</div>
    <div class="photo" role="img" aria-label="Photo of a clinician operating apheresis equipment" style="left:14px;top:160px;width:38px;height:70px;background:linear-gradient(135deg,#e3e8ec,#9fb3c2)"></div>
    <p class="body" style="position:absolute;left:58px;top:160px;width:178px">Yes. One of the most exciting new therapies available to treat autoimmune diseases is therapeutic apheresis, and HKS is at the forefront of delivering these specialized treatments. HKS utilizes state-of-the-art modern equipment to perform cell separation therapy in the treatment of a wide range of diseases, including myasthenia gravis, autoimmune neuropathy, and thrombotic thrombocytopenia purpura. HKS offers therapeutic apheresis on the same 24/7/365 basis as our inpatient dialysis services, including weekends and holidays. Other providers not rooted in rapid-response, around-the-clock service tend to prefer normal business hours. Often, our hospital clients' patients need us during other than normal business hours, and we respond accordingly.</p>
    <div class="q" style="position:absolute;left:14px;top:252px;width:222px">If our facility agrees to contract with HKS for inpatient dialysis and related services, how quickly can the transition from our current dialysis provider to HKS be completed?</div>
    <p class="body" style="position:absolute;left:14px;top:284px;width:130px">The transition can occur overnight in many cases. We have a dedicated transition team that takes care of these situations so that your facility never experiences a lapse in inpatient dialysis coverage.</p>
    <div class="photo" role="img" aria-label="Photo of a patient's arm during treatment" style="left:154px;top:280px;width:84px;height:40px;background:linear-gradient(135deg,#e8d6c6,#b88f77)"></div>
    <div class="web" style="position:absolute;left:0;top:325px;width:62%">www.harborlinekidney.example</div>
  </section>
</div>

</body>
</html>
```